Business Landing Page for SEO Company

Need the landing page of the website designed - I will provide the copy, will need to include details of my company and the services offered, about us, testimonials, faq, etc., and all these elements will need to be arranged graphically on the page.

I want something similar to this: https://plorvantix.com/

Not in terms of color or theme or anything, but we offer a similar service and want to display similar information.

Th services we provide are:

Premium Links
Monthly Links Subscription
Link Insertions

Need to advertise them on the front page. Additionally need a place for testimonials, company details, etc.,

We already have logo for the website. Please use the attached file to insert the logo within the overal design.
Updates

Target Market(s)

SEO marketers and agencies

Number of Pages Required

1 page

```html
<!DOCTYPE html>
<html lang="en">
<head>
<meta charset="utf-8">
<title>Linkwave – Link Building Services</title>
<link href="https://fonts.googleapis.com/css2?family=Josefin+Sans:ital,wght@0,300;0,400;0,600;0,700;1,300;1,400&display=swap" rel="stylesheet">
<style>
:root{
  --orange:#ff8000;
  --blue:#2f80e0;
  --blue-dark:#1f6fd0;
  --ink:#1b1b1b;
  --text:#555;
  --muted:#8a8a8a;
  --line:#d8d8d8;
  --grey-bg:#f5f5f5;
  --blog-bg:#efefef;
  --footer:#262a31;
  --white:#fff;
}
*{box-sizing:border-box;margin:0;padding:0}
html,body{width:1200px;height:4898px;overflow:hidden}
body{font-family:"Josefin Sans",sans-serif;color:var(--text);background:var(--white);position:relative}
section,footer{position:absolute;left:0;width:1200px;overflow:hidden}
.abs{position:absolute}
.btn{position:absolute;display:flex;align-items:center;justify-content:center;border-radius:30px;color:var(--white);font-weight:700;text-transform:uppercase;font-size:13px;letter-spacing:.3px}
.btn-orange{background:var(--orange)}
.btn-blue{background:var(--blue)}
.section-title{position:absolute;left:0;width:100%;text-align:center;font-weight:600;color:var(--ink);font-size:38px;letter-spacing:-.5px}
.rule{position:absolute;width:44px;height:3px;background:var(--blue)}

/* hero */
.hero{top:0;height:675px}
.hero-photo{position:absolute;inset:0;background:linear-gradient(120deg,#8c8a86 0%,#5e5a55 45%,#3e3c3a 100%)}
.hero-shade{position:absolute;inset:0;background:rgba(0,0,0,.35)}
.brand{font-weight:700;letter-spacing:-1px}
.hero .brand{top:68px;left:0;width:100%;text-align:center;font-size:60px;color:var(--white)}
.hero-title{top:246px;left:0;width:100%;text-align:center;color:var(--white);font-weight:700;font-size:58px;line-height:64px}
.hero-title .hl{color:var(--orange)}
.hero-sub{top:392px;left:300px;width:600px;text-align:center;color:var(--white);font-size:17px;line-height:30px;font-weight:300}
.hero .btn{left:474px;top:479px;width:254px;height:48px;font-size:14px}

/* services */
.services{top:675px;height:482px}
.services .section-title{top:70px}
.service-card{position:absolute;top:143px;width:261px;height:262px;border:1px solid var(--line);background:var(--white);padding:34px 28px}
.service-card.active{border:2px solid var(--orange);box-shadow:0 6px 14px rgba(0,0,0,.12)}
.service-card svg{width:50px;height:50px}
.service-card h3{margin-top:20px;font-size:21px;font-weight:600;color:var(--ink)}
.service-card p{margin-top:12px;font-size:12.5px;line-height:22px;color:var(--muted)}

/* about */
.about{top:1157px;height:618px;background:var(--grey-bg)}
.about-block{left:184px;top:336px;width:244px;height:206px;background:var(--orange)}
.about-frame{left:327px;top:75px;width:243px;height:244px;border:2px solid var(--orange)}
.about-photo{left:200px;top:89px;width:355px;height:439px;background:linear-gradient(160deg,#d9dde2,#8a9aa8 60%,#5d6670)}
.about-copy{left:612px;top:125px;width:350px}
.about-copy h2{font-size:38px;font-weight:600;color:var(--ink)}
.about-copy .rule{position:static;display:block;margin:16px 0 22px}
.about-copy p{font-size:12.5px;line-height:26px;color:var(--text);margin-bottom:26px}
.about .btn{left:612px;top:450px;width:187px;height:40px;font-size:11px;background:var(--blue)}

/* testimonials */
.testimonials{top:1775px;height:492px;background:var(--orange);color:var(--white);text-align:center}
.testimonials .quote-mark{left:570px;top:72px}
.testimonials h2{position:absolute;top:142px;left:0;width:100%;font-size:46px;font-weight:700}
.testimonials blockquote{position:absolute;top:226px;left:180px;width:840px;font-size:21px;line-height:34px;font-style:italic;font-weight:300}
.testimonials cite{position:absolute;top:333px;left:0;width:100%;font-style:normal;font-weight:700;font-size:14px}
.dots{position:absolute;top:384px;left:555px;display:flex;gap:22px}
.dot{width:14px;height:14px;border:1.5px solid var(--white);border-radius:50%;position:relative}
.dot.on::after{content:"";position:absolute;inset:3px;border-radius:50%;background:var(--white)}
.arrow-btn{position:absolute;top:250px;width:38px;height:38px;border:1.5px solid var(--white);border-radius:50%}

/* partners */
.partners{top:2267px;height:107px;border-bottom:2px solid #e6e6e6}
.partner-badge{position:absolute;top:40px;height:28px;background:#333;border-radius:3px}

/* company */
.company{top:2374px;height:483px}
.company h2{position:absolute;left:184px;top:108px;font-size:38px;font-weight:600;color:var(--ink)}
.company .rule{left:184px;top:158px;background:var(--blue)}
.company p{position:absolute;left:184px;top:182px;width:390px;font-size:12.5px;line-height:26px;color:var(--text)}
.company .btn{left:184px;top:359px;width:187px;height:40px;font-size:11px}
.company-illustration{left:605px;top:70px;width:413px;height:337px;border-radius:12px;background:radial-gradient(circle at 50% 40%,#cfe6ea,#e9f1f4 60%,#f6f8f9)}

/* faq */
.faq{top:2857px;height:576px;background:linear-gradient(135deg,var(--blue),var(--blue-dark))}
.faq h2{position:absolute;top:78px;left:0;width:100%;text-align:center;font-size:38px;font-weight:600;color:var(--white)}
.faq-item{position:absolute;left:255px;width:690px;background:var(--white);border-radius:2px;padding:0 18px}
.faq-q{height:42px;display:flex;align-items:center;font-size:12px;color:var(--muted)}
.faq-q span{flex:1}
.faq-q b{font-weight:400;margin-right:12px}
.faq-toggle{width:22px;height:22px}
.faq-a{padding:0 26px 18px 42px;font-size:11px;line-height:18px;color:var(--muted)}

/* contact */
.contact{top:3433px;height:632px}
.contact .section-title{top:72px}
.field{position:absolute;border:1px solid var(--line);display:flex;align-items:flex-start;padding:18px 16px 0;font-size:12.5px;color:#444;gap:8px}
.field svg{width:13px;height:13px;flex:none}
.contact .btn{left:523px;top:512px;width:156px;height:42px;font-size:11px}

/* blog */
.blog{top:4065px;height:563px;background:var(--blog-bg)}
.blog .section-title{top:70px}
.blog-card{position:absolute;top:138px;width:261px;height:348px;background:var(--white)}
.blog-img{height:181px}
.blog-card h3{margin:38px 18px 0;font-size:15px;line-height:19px;font-weight:600;color:var(--ink)}
.blog-card p{margin:16px 18px 0;font-size:10.5px;line-height:18px;color:var(--muted)}
.read-more{margin:12px 18px 0;font-size:11px;color:var(--blue);display:flex;align-items:center;gap:8px}

/* footer */
.site-footer{top:4628px;height:270px;background:var(--footer);color:#cfd3d8}
.site-footer .brand{position:absolute;left:202px;top:80px;font-size:40px;color:var(--blue)}
.social{position:absolute;left:212px;top:138px;display:flex;gap:8px}
.social span{width:24px;height:24px;border:1.5px solid #cfd3d8;border-radius:50%}
.foot-col{position:absolute;top:58px}
.foot-col h4{font-size:12px;font-weight:700;color:var(--white);margin-bottom:8px}
.foot-col .rule{position:static;display:block;width:38px;height:2px;margin-bottom:12px}
.foot-col li{list-style:none;font-size:10px;line-height:22px}
.newsletter{position:absolute;left:799px;top:115px;width:217px;height:30px;border-radius:20px;background:var(--white);display:flex;align-items:center;padding:2px 2px 2px 14px;font-size:10px;color:#999}
.newsletter span{flex:1}
.newsletter b{background:var(--blue);color:var(--white);height:24px;padding:0 18px;border-radius:16px;display:flex;align-items:center;font-size:10px}
.foot-bottom{position:absolute;left:184px;right:184px;top:242px;display:flex;justify-content:space-between;font-size:9.5px;color:#a0a6ad}
</style>
</head>
<body>

<section class="hero">
  <div class="hero-photo" role="img" aria-label="Photo of two businessmen reviewing documents at an office desk with a laptop"></div>
  <div class="hero-shade"></div>
  <div class="abs brand">Linkwave</div>
  <h1 class="abs hero-title">BEST <span class="hl">LINK</span><br><span class="hl">BUILDING</span> SERVICES</h1>
  <p class="abs hero-sub">Lorem ipsum dolor sit amet, consectetur adipiscing elit, sed do eiusmod tempor incididunt ut labore et dolore magna.</p>
  <a class="btn btn-orange">View our services</a>
</section>

<section class="services">
  <h2 class="section-title">OUR SERVICES</h2>
  <article class="service-card" style="left:184px">
    <svg viewBox="0 0 50 50" fill="none" stroke="#2f80e0" stroke-width="2"><path d="M14 8l5 5 6-7 6 7 5-5-2 14H16z"/><path d="M6 36l10-6h10l-2 4h-8M8 44l8-4h14l14-10-4-3-10 6"/></svg>
    <h3>Premium Links</h3>
    <p>Lorem ipsum dolor sit amet, adipg elit, sed do eiusmod tempor incididunt ut labore et dolore magna aliqua quis ipsum.</p>
  </article>
  <article class="service-card active" style="left:470px">
    <svg viewBox="0 0 50 50" fill="none" stroke="#ff8000" stroke-width="2"><rect x="6" y="6" width="38" height="22" rx="2"/><path d="M12 12h10M12 18h6M28 12h10M30 18h8"/><path d="M22 46V26a3 3 0 016 0v8l8 2v10"/></svg>
    <h3>Premium Links</h3>
    <p>Lorem ipsum dolor sit amet, adipg elit, sed do eiusmod tempor incididunt ut labore et dolore magna aliqua quis ipsum.</p>
  </article>
  <article class="service-card" style="left:755px">
    <svg viewBox="0 0 50 50" fill="none" stroke="#2f80e0" stroke-width="2"><rect x="6" y="6" width="38" height="28" rx="2"/><path d="M6 12h38M25 42V20M19 26l6-6 6 6M16 44h18"/></svg>
    <h3>Premium Links</h3>
    <p>Lorem ipsum dolor sit amet, adipg elit, sed do eiusmod tempor incididunt ut labore et dolore magna aliqua quis ipsum.</p>
  </article>
</section>

<section class="about">
  <div class="abs about-block"></div>
  <div class="abs about-frame"></div>
  <div class="abs about-photo" role="img" aria-label="Photo of a man cheering in front of computer monitors showing charts"></div>
  <div class="abs about-copy">
    <h2>ABOUT US</h2>
    <span class="rule"></span>
    <p>Lorem ipsum dolor sit amet, cour adipiscing elit, sed do eiusmod tempor incididunt ut labore et dolore magna aliqua. Quis ipsum suspendisse ultrices gravida. Risus commodo viverra maecenas accumsan lacus vel facilisis lorem ipsum dolor sit amet.</p>
    <p>Cour adipiscing elit, sed do eiusmod tempor incididunt ut labore et dolore magna aliqua quis ipsum suspendisse ultrices gravida.Risus commodo viverra maecenas.</p>
  </div>
  <a class="btn btn-blue">View our services</a>
</section>

<section class="testimonials">
  <svg class="abs quote-mark" width="60" height="48" viewBox="0 0 60 48" fill="#fff"><path d="M4 46V26C4 12 10 4 24 2v8c-7 2-10 6-10 14h10v22zM34 46V26C34 12 40 4 54 2v8c-7 2-10 6-10 14h10v22z"/></svg>
  <h2>WHAT OUR CLIENTS SAID</h2>
  <blockquote>Lorem ipsum dolor sit amet, consectetur adipiscing elit, sed do eiusmod tempor incididunt ut labore et dolore magna aliqua. Ut enim ad minim veniam, quis nostrud exercitation ullamco laboris nisi ut aliquip ex.</blockquote>
  <cite>JONATHAN DOE</cite>
  <div class="dots"><span class="dot on"></span><span class="dot"></span><span class="dot"></span></div>
  <span class="arrow-btn" style="left:72px"><svg width="35" height="35" viewBox="0 0 35 35" fill="none" stroke="#fff" stroke-width="1.6"><path d="M20 11l-6 6.5 6 6.5"/></svg></span>
  <span class="arrow-btn" style="left:1090px"><svg width="35" height="35" viewBox="0 0 35 35" fill="none" stroke="#fff" stroke-width="1.6"><path d="M15 11l6 6.5-6 6.5"/></svg></span>
</section>

<section class="partners" aria-label="Featured in">
  <span class="partner-badge" style="left:184px;width:86px"></span>
  <span class="partner-badge" style="left:344px;width:60px"></span>
  <span class="partner-badge" style="left:485px;width:72px"></span>
  <span class="partner-badge" style="left:636px;width:68px"></span>
  <span class="partner-badge" style="left:768px;width:96px"></span>
  <span class="partner-badge" style="left:916px;width:100px"></span>
</section>

<section class="company">
  <h2>OUR COMPANY</h2>
  <span class="rule"></span>
  <p>Lorem ipsum dolor sit amet, cour adipiscing elit, sed do eiusmod tempor incididunt ut labore et dolore magna aliqua. Quis ipsum suspendisse ultrices gravida. Risus commodo viverra maecenas accumsan lacus vel facilisis. Lorem ipsum dolor sit amet, cour adipiscing elit, sed do eiusmod tempor incididunt ut labore et dolore magna aliqua quis ipsum suspendisse ultrices gravida.</p>
  <a class="btn btn-blue">View our services</a>
  <div class="abs company-illustration" role="img" aria-label="Isometric illustration of a monitor with a chain link connected by arrows to web pages"></div>
</section>

<section class="faq">
  <h2>FAQ’s</h2>
  <div class="faq-item" style="top:144px"><div class="faq-q"><b>Q1.</b><span>Lorem ipsum dolor sit amet, consectetur adipiscing elit, sed do eiusmod tempor incididunt ut..?</span><svg class="faq-toggle" viewBox="0 0 22 22" fill="none" stroke="#2f80e0" stroke-width="1.4"><circle cx="11" cy="11" r="10"/><path d="M11 6v10M6 11h10"/></svg></div></div>
  <div class="faq-item" style="top:213px"><div class="faq-q"><b>Q2.</b><span>Lorem ipsum dolor sit amet, consectetur adipiscing elit, sed do eiusmod tempor incididunt ut..?</span><svg class="faq-toggle" viewBox="0 0 22 22" fill="none" stroke="#2f80e0" stroke-width="1.4"><circle cx="11" cy="11" r="10"/><path d="M11 6v10M6 11h10"/></svg></div></div>
  <div class="faq-item" style="top:283px"><div class="faq-q"><b>Q3.</b><span>Lorem ipsum dolor sit amet, consectetur adipiscing elit, sed do eiusmod tempor incididunt ut..?</span><svg class="faq-toggle" viewBox="0 0 22 22" fill="none" stroke="#2f80e0" stroke-width="1.4"><circle cx="11" cy="11" r="10"/><path d="M11 6v10M6 11h10"/></svg></div></div>
  <div class="faq-item" style="top:352px"><div class="faq-q"><b>Q4.</b><span>Lorem ipsum dolor sit amet, consectetur adipiscing elit, sed do eiusmod tempor incididunt ut..?</span><svg class="faq-toggle" viewBox="0 0 22 22" fill="none" stroke="#2f80e0" stroke-width="1.4"><circle cx="11" cy="11" r="10"/><path d="M6 11h10"/></svg></div>
    <p class="faq-a">Lorem ipsum dolor sit amet, consectetur adipiscing elit, sed do eiusmod tempor incididunt ut labore et dolore magna aliqua. Quis ipsum suspendisse ultrices gravida. Risus commodo viverra maecenas accumsan lacus vel facilisis. Lorem ipsum dolor sit amet, consectetur adipiscing elit, sed do eiusmod tempor incididunt ut labore et dolore magna aliqua.</p>
  </div>
</section>

<section class="contact">
  <h2 class="section-title">CONTACT US</h2>
  <div class="field" style="left:255px;top:143px;width:333px;height:49px;padding-top:17px"><svg viewBox="0 0 13 13" fill="#777"><circle cx="6.5" cy="3.5" r="3"/><path d="M1 13c0-4 2.5-6 5.5-6s5.5 2 5.5 6z"/></svg>First Name</div>
  <div class="field" style="left:611px;top:143px;width:334px;height:49px;padding-top:17px"><svg viewBox="0 0 13 13" fill="#777"><circle cx="6.5" cy="3.5" r="3"/><path d="M1 13c0-4 2.5-6 5.5-6s5.5 2 5.5 6z"/></svg>Last Name</div>
  <div class="field" style="left:255px;top:215px;width:333px;height:49px;padding-top:17px"><svg viewBox="0 0 13 13" fill="#777"><path d="M2 1l3 .5 1 3-1.5 1.5a7 7 0 003.5 3.5L9.5 8l3 1 .5 3-2 1C5 13 0 8 0 3z"/></svg>Mobile Number</div>
  <div class="field" style="left:611px;top:215px;width:334px;height:49px;padding-top:17px"><svg viewBox="0 0 13 13" fill="#777"><path d="M0 2h13v9H0z"/><path d="M0 2l6.5 5L13 2" stroke="#fff" fill="none"/></svg>Email Address</div>
  <div class="field" style="left:255px;top:289px;width:690px;height:177px"><svg viewBox="0 0 13 13" fill="#777"><path d="M1 1h9v7H4l-3 3z"/><path d="M11 4h2v8l-2-2H5V9" /></svg>Your Message</div>
  <a class="btn btn-blue">Submit now!</a>
</section>

<section class="blog">
  <h2 class="section-title">BLOG ARTICLES</h2>
  <article class="blog-card" style="left:184px">
    <div class="blog-img" role="img" aria-label="Photo of large patterned SEO letters on a white surface" style="background:linear-gradient(135deg,#f2f2f2,#d6d6d6)"></div>
    <h3>Lorem ipsum dolor sit amet, consectetur.</h3>
    <p>Lorem ipsum dolor sit amet, consectetur adipiscing elit, sed do eiusmod.</p>
    <div class="read-more">Read More <svg width="14" height="8" viewBox="0 0 14 8" fill="none" stroke="#2f80e0" stroke-width="1.4"><path d="M0 4h13M10 1l3 3-3 3"/></svg></div>
  </article>
  <article class="blog-card" style="left:470px">
    <div class="blog-img" role="img" aria-label="Photo of hands typing on a laptop showing an analytics dashboard" style="background:linear-gradient(135deg,#b9c6d4,#6f8196)"></div>
    <h3>Lorem ipsum dolor sit amet, consectetur.</h3>
    <p>Lorem ipsum dolor sit amet, consectetur adipiscing elit, sed do eiusmod.</p>
    <div class="read-more">Read More <svg width="14" height="8" viewBox="0 0 14 8" fill="none" stroke="#2f80e0" stroke-width="1.4"><path d="M0 4h13M10 1l3 3-3 3"/></svg></div>
  </article>
  <article class="blog-card" style="left:755px">
    <div class="blog-img" role="img" aria-label="Photo of a laptop with a trading chart on a desk" style="background:linear-gradient(135deg,#c9ced4,#5b6068)"></div>
    <h3>Lorem ipsum dolor sit amet, consectetur.</h3>
    <p>Lorem ipsum dolor sit amet, consectetur adipiscing elit, sed do eiusmod.</p>
    <div class="read-more">Read More <svg width="14" height="8" viewBox="0 0 14 8" fill="none" stroke="#2f80e0" stroke-width="1.4"><path d="M0 4h13M10 1l3 3-3 3"/></svg></div>
  </article>
</section>

<footer class="site-footer">
  <div class="brand">Linkwave</div>
  <div class="social" aria-label="Social links"><span></span><span></span><span></span><span></span></div>
  <div class="foot-col" style="left:388px"><h4>Quick Links</h4><span class="rule"></span><ul><li>Home</li><li>Testimonials</li><li>News</li><li>FAQ’s</li></ul></div>
  <div class="foot-col" style="left:515px"><h4>About Us</h4><span class="rule"></span><ul><li>About Us</li><li>Our Company</li></ul></div>
  <div class="foot-col" style="left:630px"><h4>Services</h4><span class="rule"></span><ul><li>Premium Links</li><li>Monthly Links Subscription</li><li>Link Insertions</li></ul></div>
  <div class="foot-col" style="left:799px"><h4>Subscribe Our Newsletter</h4><span class="rule"></span></div>
  <div class="newsletter"><span>Email...</span><b>Subscribe!</b></div>
  <div class="foot-bottom"><span>© Copyright Linkwave 2021, All Rights Reserved.</span><span>Privacy Policy &nbsp;|&nbsp; Terms &amp; Conditions</span></div>
</footer>

</body>
</html>
```